Design a double sided business card

We are looking for a clean, eye-catching, and contemporary design that enhances the brand and presents a premium, professional image. Our preference is for a brown card with black gloss detailing and embossed elements; however, we are open to creative input and design suggestions that best achieve a strong visual impact.

Please see the attached existing business card for reference. We use both black and brown colours consistently across our branding.

On sample provided

```html
<!DOCTYPE html>
<html lang="en">
<head>
<meta charset="utf-8">
<title>Halden – Business Card</title>
<link href="https://fonts.googleapis.com/css2?family=Poppins:wght@400;500;700&display=swap" rel="stylesheet">
<style>
  :root {
    --backdrop: #2b2b2d;
    --card: #111112;
    --tan: #c9b394;
    --text-light: #f2f2f2;
    --rule-grey: #5a5a5a;
  }
  * { box-sizing: border-box; margin: 0; padding: 0; }
  html, body {
    width: 1200px; height: 952px; overflow: hidden;
    background: var(--backdrop);
    font-family: "Poppins", sans-serif;
  }
  .sheet {
    width: 1200px; height: 952px;
    display: flex; flex-direction: column; align-items: center; justify-content: center;
    gap: 48px;
  }
  .card {
    position: relative;
    width: 640px; height: 366px;
    background: var(--card);
    box-shadow: 0 14px 34px rgba(0,0,0,.45);
  }
  .card__frame {
    position: absolute; inset: 30px;
    border: 1px solid var(--tan);
  }

  /* Front side */
  .front__wordmark {
    position: absolute; left: 0; right: 0; top: 136px;
    text-align: center;
    color: var(--tan);
    font-weight: 700; font-size: 62px; letter-spacing: 10px;
    line-height: 1;
  }
  .front__web {
    position: absolute; left: 50%; bottom: 21px;
    transform: translateX(-50%);
    background: var(--card);
    padding: 0 18px;
    color: var(--text-light);
    font-size: 13px; letter-spacing: 4.5px;
  }

  /* Back side */
  .brand {
    position: absolute; left: 72px; top: 98px; width: 220px;
    display: flex; flex-direction: column; align-items: center; gap: 16px;
  }
  .brand__square {
    width: 86px; height: 86px;
    border: 5px solid var(--tan);
  }
  .brand__name {
    color: var(--tan);
    font-weight: 700; font-size: 34px; letter-spacing: 6px; line-height: 1;
  }
  .contact {
    position: absolute; left: 330px; top: 92px; width: 260px;
  }
  .contact__name {
    color: var(--tan);
    font-weight: 700; font-size: 27px; line-height: 1.1;
  }
  .contact__role {
    display: inline-block;
    color: var(--text-light);
    font-size: 13px; margin-top: 2px; padding-bottom: 3px;
    border-bottom: 1px solid var(--rule-grey);
  }
  .contact__list { list-style: none; margin-top: 14px; }
  .contact__item {
    display: flex; align-items: flex-start; gap: 10px;
    color: var(--text-light);
    font-size: 12px; line-height: 1.35;
    margin-bottom: 9px;
  }
  .contact__icon {
    flex: none; width: 17px; height: 17px;
    background: var(--tan); border-radius: 3px;
    display: flex; align-items: center; justify-content: center;
  }
  .contact__icon svg { width: 11px; height: 11px; fill: var(--card); }
</style>
</head>
<body>
<main class="sheet">

  <section class="card card--front" aria-label="Card front">
    <div class="card__frame"></div>
    <div class="front__wordmark">HALDEN</div>
    <div class="front__web">www.halden.co.uk</div>
  </section>

  <section class="card card--back" aria-label="Card back">
    <div class="card__frame"></div>

    <div class="brand">
      <div class="brand__square"></div>
      <div class="brand__name">HALDEN</div>
    </div>

    <div class="contact">
      <h1 class="contact__name">RAVI DALTON</h1>
      <span class="contact__role">Director</span>
      <ul class="contact__list">
        <li class="contact__item">
          <span class="contact__icon"><svg viewBox="0 0 24 24"><path d="M12 2a7 7 0 0 0-7 7c0 5 7 13 7 13s7-8 7-13a7 7 0 0 0-7-7zm0 9.5A2.5 2.5 0 1 1 12 6.5a2.5 2.5 0 0 1 0 5z"/></svg></span>
          <span>12 Marsh Farm Road<br>Eastbrook EB4 2LP</span>
        </li>
        <li class="contact__item">
          <span class="contact__icon"><svg viewBox="0 0 24 24"><path d="M6.6 10.8a15 15 0 0 0 6.6 6.6l2.2-2.2a1 1 0 0 1 1-.25 11.4 11.4 0 0 0 3.6.57 1 1 0 0 1 1 1V20a1 1 0 0 1-1 1A17 17 0 0 1 3 4a1 1 0 0 1 1-1h3.5a1 1 0 0 1 1 1c0 1.25.2 2.45.57 3.57a1 1 0 0 1-.25 1z"/></svg></span>
          <span>0800 000 4172</span>
        </li>
        <li class="contact__item">
          <span class="contact__icon"><svg viewBox="0 0 24 24"><path d="M7 1h10a2 2 0 0 1 2 2v18a2 2 0 0 1-2 2H7a2 2 0 0 1-2-2V3a2 2 0 0 1 2-2zm0 3v14h10V4zm5 15.5a1 1 0 1 0 0 2 1 1 0 0 0 0-2z"/></svg></span>
          <span>07700 900431</span>
        </li>
        <li class="contact__item">
          <span class="contact__icon"><svg viewBox="0 0 24 24"><path d="M2 5h20v14H2zm2 2v.5l8 5 8-5V7zm0 2.8V17h16V9.8l-8 5z"/></svg></span>
          <span>ravi@halden.co.uk</span>
        </li>
      </ul>
    </div>
  </section>

</main>
</body>
</html>
```